New Corporate website more focused on funnel and great design

Our company, Bold Harbor needs a new website to look like it's from 2021. We work with large businesses in the corporte world and need to reflect that we are professional, focused on our clients, and trsutworthy. It should include some/most of the components from our current site: boldharbor.com but should focus more about getting people to optin to out free downloads, which can be found on this page: https://www.boldharbor.com/get-started-with-a-prep-session/ and this page: https://www.boldharbor.com/team-onboarding/

Our new website should do a better job at explaining what we do, who we serve, and how we fix their problems of onboarding new leaders. Feel free to use dummy text if you are not sure what to put in for certain sections. I also would like to point out that most of the audiance is older, so we don't need anything too younge and flashy, or that is hard it use. it should have big clear fonts, plently of contrast, and work well for poeple who are not good at using the internet. Please use the colors of the logo, and you can add another color or two if you think it's fits

Industry/Entity Type

business consulting

Number of Pages Required

2 page

Font styles to use
Sans Serif

Requirements
Must have
• corporate feel, look professional, focus on getting new leads
Should not have
• cute or children feel

```html
<!DOCTYPE html>
<html lang="en">
<head>
<meta charset="utf-8">
<title>Bold Harbor — Better Results Faster</title>
<link rel="stylesheet" href="https://fonts.googleapis.com/css2?family=Montserrat:wght@400;600;700;800&family=Roboto:ital,wght@0,300;0,400;0,500;0,700;1,300;1,400&display=swap">
<style>
:root{
  --navy:#1a3c72;
  --navy-deep:#13305e;
  --blue:#2c8bd3;
  --blue-bright:#2f9be6;
  --testimonial:#1f4c95;
  --ink:#1f2430;
  --text:#555b66;
  --grey-bg:#efefef;
  --dark:#262626;
  --footer:#1b2b4b;
  --topbar:#1d1d1f;
  --yellow:#f5c518;
  --map-sea:#b7cde6;
  --map-land:#e4e7ea;
  --white:#fff;
}
*{box-sizing:border-box;margin:0;padding:0}
html,body{width:1200px;height:4428px;overflow:hidden}
body{font-family:"Roboto",sans-serif;color:var(--text);background:var(--white);position:relative}
section,header,footer,.topbar{position:absolute;left:0;width:1200px}
.abs{position:absolute}
a{color:inherit;text-decoration:none}

/* top bar */
.topbar{top:0;height:28px;background:var(--topbar);color:#cfd3da;font-size:11px}
.topbar .social{left:52px;top:9px;display:flex;gap:14px}
.topbar .social span{width:10px;height:10px;border-radius:50%;background:#cfd3da;display:block}
.topbar .phone{left:818px;top:7px}
.topbar .enquire{left:980px;top:0;width:142px;height:28px;background:var(--blue);color:#fff;font-weight:700;font-size:10px;line-height:28px;padding-left:26px}

/* header */
.site-header{top:28px;height:92px;background:#fff;border-bottom:1px solid #e6e6e6}
.brand{left:45px;top:22px;display:flex;align-items:center;gap:10px}
.brand .mark{width:44px;height:44px;background:var(--navy)}
.brand .name{font-family:"Montserrat",sans-serif;font-weight:600;font-size:28px;color:var(--navy);line-height:1}
.brand .tag{font-size:9px;letter-spacing:3px;color:var(--navy);margin-top:4px}
.nav{left:455px;top:20px;display:flex;align-items:center;font-size:11px;font-weight:700;color:var(--navy);font-family:"Montserrat",sans-serif}
.nav a{padding:0 14px;height:52px;line-height:52px}
.nav a.active{background:var(--navy);color:#fff;padding:0 18px}

/* hero */
.hero{top:120px;height:532px;background:var(--navy)}
.hero .photo{left:487px;top:0;width:713px;height:532px;background:linear-gradient(120deg,#5b7ca8 0%,#9db3cf 45%,#d8e0ea 100%);opacity:.85}
.hero .copy{left:0;top:0;width:936px;text-align:center;color:#fff}
.hero .eyebrow{position:absolute;top:174px;left:0;width:936px;font-size:11px;letter-spacing:3px;font-weight:500}
.hero h1{position:absolute;top:208px;left:0;width:936px;font-weight:300;font-size:31px}
.hero h2{position:absolute;top:246px;left:0;width:936px;font-weight:700;font-size:42px}
.hero .btn{position:absolute;top:324px;left:396px;width:180px;height:44px;background:var(--blue);color:#fff;font-size:13px;line-height:44px;text-align:center}

/* band */
.band{top:652px;height:130px;background:var(--blue)}
.band p{position:absolute;left:0;width:1005px;text-align:center;color:#fff}
.band .lead{top:24px;font-size:25px;font-style:italic;font-weight:300}
.band .big{top:58px;font-size:39px;font-weight:700}
.band .btn{position:absolute;left:949px;top:40px;width:139px;height:44px;background:var(--navy);color:#fff;font-size:12px;font-weight:700;line-height:44px;text-align:center}

/* services */
.services{top:782px;height:608px;background:#fff}
.card{position:absolute;top:114px;width:310px;height:425px;background:#f4f4f4;box-shadow:0 2px 10px rgba(0,0,0,.12)}
.card .img{height:144px;background:linear-gradient(135deg,#a9b9cc,#e1e6ec)}
.card .img.tech{background:linear-gradient(135deg,#2b5c9c,#7fa6d2)}
.card .label{height:78px;background:var(--navy-deep);color:#fff;padding:18px 0 0 88px;position:relative}
.card .label .icon{position:absolute;left:26px;top:18px;width:40px;height:40px;border:2px solid #7fb7e8;border-radius:50%}
.card .label h3{font-size:17px;font-weight:500}
.card .label em{font-size:13px;font-weight:300}
.card p.body{padding:18px 12px 0;font-size:12.5px;line-height:25px;color:#666;text-align:justify}
.card .more{position:absolute;left:20px;bottom:24px;font-size:11px;font-weight:700;color:var(--navy)}

/* who */
.who{top:1390px;height:613px;background:var(--grey-bg)}
.section-title{position:absolute;left:0;width:1200px;text-align:center;font-family:"Montserrat",sans-serif;font-weight:700;font-size:31px;color:var(--ink)}
.section-title::after{content:"";display:block;width:30px;height:4px;background:var(--blue);margin:14px auto 0}
.section-sub{position:absolute;left:0;width:1200px;text-align:center;font-family:"Montserrat",sans-serif;font-size:15px;color:#6d727b}
.who .visual{left:139px;top:202px;width:334px;height:329px;background:linear-gradient(160deg,#1e5eb0,#3a8fdd 60%,#b8d5ef)}
.who .since{left:218px;top:332px;width:238px;height:74px;background:var(--navy-deep);color:#fff;text-align:center}
.who .since small{display:block;font-size:11px;letter-spacing:2px;font-weight:700;margin-top:12px}
.who .since b{font-family:"Montserrat",sans-serif;font-size:29px;font-weight:800}
.who .text{left:526px;top:202px;width:528px;font-size:12.5px;line-height:26.5px;color:#666}
.who .text p+p{margin-top:26px}
.who .btn{left:526px;top:502px;width:108px;height:30px;background:var(--blue);color:#fff;font-size:10px;font-weight:700;line-height:30px;text-align:center}

/* testimonials */
.testimonials{top:2003px;height:444px;background:var(--testimonial);overflow:hidden;color:#fff}
.testimonials .deco{left:700px;top:-20px;width:540px;height:500px;border-radius:50%;background:rgba(255,255,255,.06)}
.testimonials h2{position:absolute;top:60px;left:0;width:1200px;text-align:center;font-family:"Montserrat",sans-serif;font-weight:700;font-size:31px;color:var(--blue-bright)}
.testimonials .rule{left:585px;top:113px;width:30px;height:4px;background:#fff}
.testimonials .sub{top:133px;left:0;width:1200px;text-align:center;font-family:"Montserrat",sans-serif;font-size:15px}
.testimonials .quote{top:196px;left:0;width:1200px;text-align:center;font-style:italic;font-size:15px;line-height:31px}
.testimonials .avatar{left:565px;top:278px;width:82px;height:82px;border-radius:50%;background:linear-gradient(135deg,#c9a58a,#8a6a55)}
.testimonials .who-said{top:372px;left:0;width:1200px;text-align:center;font-size:13px;font-weight:700}
.arrow{position:absolute;top:200px}

/* blog */
.blog{top:2447px;height:605px;background:#fff}
.post{position:absolute;top:178px;width:225px}
.post .img{height:160px;background:linear-gradient(135deg,#4b5462,#a3a9b2)}
.post .bar{width:40px;height:4px;background:#8c8cf0;margin:26px 0 12px}
.post h3{font-family:"Montserrat",sans-serif;font-size:13px;font-weight:600;line-height:21px;color:var(--navy)}
.post time{display:block;font-size:10px;color:#888;margin-top:12px;padding-left:20px;position:relative}
.post time::before{content:"";position:absolute;left:0;top:0;width:10px;height:10px;border:2px solid var(--blue);border-radius:50%}
.blog .btn{left:547px;top:514px;width:130px;height:30px;background:var(--blue);color:#fff;font-size:10px;font-weight:700;line-height:30px;text-align:center}

/* clients */
.clients{top:3052px;height:352px;background:#fff}
.clients h2{position:absolute;top:46px;left:0;width:1200px;text-align:center;font-family:"Montserrat",sans-serif;font-weight:400;font-size:27px;color:var(--ink)}
.clients h2 b{font-weight:700;color:var(--navy)}
.clients h2 b.hl{color:var(--blue)}
.logos{position:absolute;top:130px;left:60px;width:1080px;display:flex;justify-content:space-around;align-items:center;height:90px}
.logos span{font-family:"Montserrat",sans-serif;font-weight:700;font-size:34px;color:var(--navy);display:flex;align-items:center;gap:10px}
.logos span i{width:22px;height:22px;background:var(--navy);display:block}
.clients .more{position:absolute;top:285px;left:0;width:1200px;text-align:center;font-size:13px;color:var(--navy)}

/* contact */
.contact{top:3404px;height:326px;background:var(--dark);color:#fff}
.contact h2{position:absolute;left:112px;top:100px;font-family:"Montserrat",sans-serif;font-weight:800;font-size:32px;line-height:38px}
.contact .accent{left:112px;top:186px;width:30px;height:4px;background:var(--yellow)}
.contact .intro{left:112px;top:206px;width:300px;font-size:11px;line-height:22px}
.contact .label{left:446px;top:64px;font-size:12px;font-weight:700}
.field{position:absolute;width:308px;height:42px;background:#e3e3e3;color:#555;font-size:12px;line-height:42px;padding-left:24px}
.contact .submit{left:446px;top:246px;width:116px;height:42px;background:var(--navy);font-size:13px;font-weight:700;line-height:42px;padding-left:24px}

/* location area */
.map{top:3730px;height:303px;background:linear-gradient(100deg,var(--map-sea) 0%,var(--map-land) 45%,var(--map-land) 75%,#d3dde8 100%)}

/* footer */
.site-footer{top:4033px;height:395px;background:var(--footer);color:#c7cfdd}
.site-footer h4{position:absolute;top:68px;font-family:"Montserrat",sans-serif;font-weight:700;font-size:21px;color:#fff}
.site-footer .col-rule{position:absolute;top:110px;width:226px;height:1px;background:#3b4d6f}
.site-footer .brand{left:112px;top:60px}
.site-footer .brand .name,.site-footer .brand .tag{color:#fff}
.site-footer .brand .mark{background:#fff}
.site-footer .small{position:absolute;font-size:11px;line-height:18px}
.site-footer .links{position:absolute;font-size:10px;color:#8fa5cc;line-height:35px}
.dot{width:26px;height:26px;border-radius:50%;background:#fff;display:inline-block;margin-right:8px}
.site-footer .subscribe{left:863px;top:100px;width:226px;height:32px;background:#fff;font-size:10px;color:#999;line-height:32px;padding-left:14px}
.site-footer .subscribe i{position:absolute;right:0;top:0;width:36px;height:32px;background:var(--blue)}
.site-footer .bottom-rule{left:112px;top:348px;width:976px;height:1px;background:#3b4d6f}
.site-footer .copy{top:364px;left:0;width:1200px;text-align:center;font-size:10px}
</style>
</head>
<body>

<div class="topbar">
  <div class="abs social"><span></span><span></span><span></span></div>
  <div class="abs phone">&#9742; (+1) 555 010 2040</div>
  <a class="abs enquire" href="#">ENQUIRE NOW &nbsp; &#9656;</a>
</div>

<header class="site-header">
  <div class="abs brand">
    <div class="mark"></div>
    <div><div class="name">Bold Harbor</div><div class="tag">BETTER RESULTS FASTER</div></div>
  </div>
  <nav class="abs nav">
    <a class="active" href="#">HOME</a><a href="#">WHO WE ARE ▾</a><a href="#">WHAT WE DO ▾</a><a href="#">CLIENTS ▾</a><a href="#">BLOG</a><a href="#">RESOURCES ▾</a><a href="#">CONTACT</a>
  </nav>
</header>

<section class="hero">
  <div class="abs photo" role="img" aria-label="Photo of two business professionals reviewing work at a laptop"></div>
  <div class="abs copy">
    <div class="eyebrow">MEET CONSULTING &nbsp;——</div>
    <h1>Accelerate Business Performance During</h1>
    <h2>Critical Leadership Transitions</h2>
    <a class="btn" href="#">JOIN US NOW &nbsp;→</a>
  </div>
</section>

<section class="band">
  <p class="lead">Get done in 100 days what normally takes 6-12 months</p>
  <p class="big">90% of Bold Harbor Clients Succeed</p>
  <a class="btn" href="#">Contact us &nbsp;→</a>
</section>

<section class="services">
  <article class="card" style="left:98px">
    <div class="img" role="img" aria-label="Photo of a smiling executive with colleagues"></div>
    <div class="label"><span class="icon"></span><h3>Executive Onboarding</h3><em>40% of new leaders fail</em></div>
    <p class="body">For executive leaders taking on new roles, the Bold Harbor 100-Day Action Plan process prepares leaders before the start, speeds up assimilation, sets direction, builds the team, accelerates momentum, and delivers results...</p>
    <a class="more" href="#">LEARN MORE →</a>
  </article>
  <article class="card" style="left:432px">
    <div class="img" role="img" aria-label="Photo of a team in a video conference meeting"></div>
    <div class="label"><span class="icon"></span><h3>Team Onboarding</h3><em>80% of M&amp;A fail to boost returns.</em></div>
    <p class="body">For leaders integrating teams post acquisition or re-organization, the Bold Harbor 100 Day Action Plan process gets all players on board with the change and accelerates achievement of cultural and business integration goals...</p>
    <a class="more" href="#">LEARN MORE →</a>
  </article>
  <article class="card" style="left:765px">
    <div class="img tech" role="img" aria-label="Illustration of a hand touching startup strategy bubbles"></div>
    <div class="label"><span class="icon"></span><h3>Acceleration &amp; Restart</h3><em>70% of transformations fall short</em></div>
    <p class="body">For executives leading through a strategic point of inflection or reinvigorating a stalled team, Bold Harbor programs define the from-to challenge, kickstart a change process and deliver results that stick...</p>
    <a class="more" href="#">LEARN MORE →</a>
  </article>
</section>

<section class="who">
  <h2 class="section-title" style="top:62px">who we are</h2>
  <p class="section-sub" style="top:132px">We Accelerate Leaders and Teams During Critical Transitions</p>
  <div class="abs visual" role="img" aria-label="Blue-toned city skyline at night"></div>
  <div class="abs since"><small>SERVING</small><b>SINCE 2003</b></div>
  <div class="abs text">
    <p><b style="color:#333">Bold Harbor</b> accelerates leaders and teams to deliver better results faster through critical transitions, leading to short term and lasting success for the leader and the organization. We create leverage when new CEO's and C-Suite executives are tasked with transforming results and there is a need for speed. Using our 100-Day Action Plan process, leaders quickly build a cohesive team, align around strategic, operational and organizational actions, and dramatically accelerate value creation.</p>
    <p>Whether you are a new C-suite executive, integrating teams as a result of an acquisition or re-organization, or you need to quickly pivot your existing team at a strategic point of inflection, we'll help you deliver better results faster.</p>
  </div>
  <a class="abs btn" href="#">LEARN MORE →</a>
</section>

<section class="testimonials">
  <div class="abs deco" role="img" aria-label="Faint oversized quotation graphic"></div>
  <h2>what our clients say</h2>
  <div class="abs rule"></div>
  <p class="abs sub">A Precious and Valuable Reviews from our Customers</p>
  <p class="abs quote">Somewhere right now, there is a first time CEO out there, not working with<br>Bold Harbor, not following their 100-Day Action Plan, and I am worried for them.</p>
  <div class="abs avatar" role="img" aria-label="Portrait of the client quoted"></div>
  <p class="abs who-said">Clara Whitford, CEO Northvale Systems</p>
  <svg class="arrow" style="left:130px" width="24" height="60" viewBox="0 0 24 60"><path d="M20 2 L4 30 L20 58" fill="none" stroke="#fff" stroke-width="2"/></svg>
  <svg class="arrow" style="left:1052px" width="24" height="60" viewBox="0 0 24 60"><path d="M4 2 L20 30 L4 58" fill="none" stroke="#fff" stroke-width="2"/></svg>
</section>

<section class="blog">
  <h2 class="section-title" style="top:56px">blog posts</h2>
  <p class="section-sub" style="top:126px">Featured Books and Recent Blog Posts</p>
  <article class="post" style="left:112px"><div class="img" role="img" aria-label="Photo of executives at a hearing table"></div><div class="bar"></div><h3>Why Meridian Oil's New CFO Should Fail, But Won't</h3><time>June 14, 2020</time></article>
  <article class="post" style="left:363px"><div class="img" role="img" aria-label="Photo of a framed print on a dark wall"></div><div class="bar"></div><h3>When To Inform In Advance Versus Report After The Fact</h3><time>April 25, 2020</time></article>
  <article class="post" style="left:612px"><div class="img" role="img" aria-label="Photo of a woman holding balloons outside an office"></div><div class="bar"></div><h3>When To Use The Three Different Ways To Fire Employees</h3><time>April 25, 2020</time></article>
  <article class="post" style="left:863px"><div class="img" role="img" aria-label="Photo of an excited sports fan in a crowd"></div><div class="bar"></div><h3>How To Elevate Involved Participants To Committed Champions</h3><time>January 22, 2020</time></article>
  <a class="abs btn" href="#">VIEW ALL POSTS →</a>
</section>

<section class="clients">
  <h2>Our <b>Top 10</b> Clients Have Used Us Over <b class="hl">180 Times</b></h2>
  <div class="logos">
    <span>Redline Print</span>
    <span><i></i>Cloudbin</span>
    <span>Ridgefield</span>
    <span>Ashcombe</span>
    <span>Vista TV</span>
  </div>
  <p class="more">Learn More About Out Worldwide Clients &nbsp;➜</p>
</section>

<section class="contact">
  <h2>speak to one of<br>our partners today</h2>
  <div class="abs accent"></div>
  <p class="abs intro">Would you like to speak to one of our financial advisers over the phone? Just submit your details and we'll be in touch shortly. You can also email us if you would prefer.</p>
  <p class="abs label">I would like to discuss:</p>
  <div class="field" style="left:446px;top:96px">Name</div>
  <div class="field" style="left:780px;top:96px">Phone</div>
  <div class="field" style="left:446px;top:166px">Email</div>
  <div class="field" style="left:780px;top:166px">Your Message</div>
  <a class="abs submit" href="#">submit &nbsp; ›</a>
</section>

<section class="map" role="img" aria-label="Map of Europe marking the three office locations"></section>

<footer class="site-footer">
  <div class="abs brand">
    <div class="mark" style="width:36px;height:36px"></div>
    <div><div class="name" style="font-size:24px">Bold Harbor</div><div class="tag">BETTER RESULTS FASTER</div></div>
  </div>
  <p class="small" style="left:120px;top:140px">&#9743; &nbsp; +1 555-010-7788</p>
  <p class="small" style="left:120px;top:172px;color:#8fa5cc">&#9993; &nbsp; hello@boldharbor.com</p>
  <div class="abs" style="left:144px;top:222px"><span class="dot"></span><span class="dot"></span><span class="dot"></span><span class="dot"></span></div>

  <h4 style="left:363px">recent news</h4><div class="col-rule" style="left:363px"></div>
  <p class="small" style="left:363px;top:130px;color:#fff;width:210px">Narrow Your Focus to Prevent Overanalysis</p>
  <p class="small" style="left:363px;top:168px;font-size:9px">◷ June 14, 2020</p>
  <p class="small" style="left:363px;top:210px;color:#fff;width:210px">Three Social Media Hacks for the Busy Entrepreneur</p>
  <p class="small" style="left:363px;top:248px;font-size:9px">◷ April 25, 2020</p>

  <h4 style="left:613px">extra links</h4><div class="col-rule" style="left:613px"></div>
  <div class="links" style="left:613px;top:112px">Home<br>Who We Are<br>What We Do<br>Clients</div>
  <div class="links" style="left:743px;top:112px">Resources<br>Blogs<br>Contact</div>

  <h4 style="left:863px">subscribe</h4>
  <div class="abs subscribe">Enter Your E-mail<i></i></div>
  <p class="small" style="left:863px;top:144px;font-size:10px">Get latest updates and offers.</p>

  <div class="abs bottom-rule"></div>
  <p class="abs copy">© 2021 Bold Harbor | BETTER RESULTS FASTER Since 2003</p>
</footer>

</body>
</html>
```